We need a fresh, new church business card!!

We need a church business card with basic info to hand out as invites. We are looking for something clean that communicates our basic information clearly.

We are open to square or rectangle card sizes.

General Public

Religious

The attached logo is the only one that I have available. We'd like to see options with with text of the logo lighter and on a dark background as well as options with white/light backgrounds.

Also, we'd like to see option with rounded corners.

• Address - 2718 Maple Row, Rockford, IL 61142
• Website - brookvane.example
• Phone - 815-555-0163
• Service times -
• Sunday - 10am Sunday School
• - 11am Family Worship
• - 6pm Night of Prayer
• Wednesday - 7:30pm Adult Bible Study
• Classes for all ages

```html
<!DOCTYPE html>
<html lang="en">
<head>
<meta charset="utf-8">
<title>Brookvane Pentecostal Church – Business Cards</title>
<link href="https://fonts.googleapis.com/css2?family=Jost:wght@400;500&display=swap" rel="stylesheet">
<style>
  :root {
    --stage: #e9e5e0;
    --card-dark: #1f1311;
    --card-light: #ffffff;
    --teal: #4e93a6;
    --ink-light: #ffffff;
    --ink-dark: #2a1d1a;
    --photo-top: #4a3733;
    --photo-bottom: #1c1210;
  }
  * { margin: 0; padding: 0; box-sizing: border-box; }
  html, body { width: 1200px; height: 1200px; overflow: hidden; }
  body {
    background: var(--stage);
    font-family: "Jost", sans-serif;
    position: relative;
  }
  .card {
    position: absolute;
    width: 784px;
    height: 453px;
    box-shadow: 0 6px 18px rgba(0,0,0,0.25);
  }
  .card--front { left: 74px; top: 173px; background: var(--card-dark); color: var(--ink-light); }
  .card--back { left: 341px; top: 655px; background: var(--card-light); color: var(--ink-dark); }

  .brand { display: flex; align-items: center; justify-content: center; gap: 22px; }
  .brand__dot { width: 66px; height: 66px; border-radius: 50%; background: var(--teal); flex: none; }
  .brand__text { display: flex; flex-direction: column; color: var(--ink-light); }
  .brand__name { font-size: 56px; line-height: 1; font-weight: 400; letter-spacing: 1px; text-transform: uppercase; }
  .brand__tag { font-size: 15px; letter-spacing: 6.4px; text-transform: uppercase; margin-top: 10px; }

  .card--front .brand { margin-top: 70px; }
  .services { text-align: center; margin-top: 36px; }
  .services__title { color: var(--teal); font-size: 30px; font-weight: 400; }
  .services__line { font-size: 23px; margin-top: 8px; line-height: 1.45; }
  .services__line b { font-weight: 500; }
  .services__mark { display: inline-block; width: 18px; height: 18px; background: var(--ink-light); margin-right: 8px; vertical-align: -1px; }
  .services__group { margin-top: 10px; }

  .banner {
    height: 226px;
    background: linear-gradient(180deg, var(--photo-top), var(--photo-bottom));
    display: flex; align-items: center; justify-content: center;
    position: relative;
  }
  .banner .brand { position: relative; }
  .banner .brand__dot { width: 84px; height: 84px; }
  .banner .brand__name { font-size: 62px; }

  .contact { text-align: center; margin-top: 36px; font-size: 27px; line-height: 41px; }
  .contact__row { display: flex; justify-content: center; align-items: center; gap: 10px; }
  .contact__item { display: inline-flex; align-items: center; gap: 6px; }
  .contact__item + .contact__item { margin-left: 12px; }
  .icon { width: 20px; height: 20px; fill: var(--ink-dark); flex: none; }
  .social-dot { width: 12px; height: 12px; border-radius: 50%; background: var(--ink-dark); display: inline-block; }
</style>
</head>
<body>

<section class="card card--front">
  <div class="brand">
    <span class="brand__dot"></span>
    <div class="brand__text">
      <span class="brand__name">Brookvane</span>
      <span class="brand__tag">Pentecostal Church</span>
    </div>
  </div>
  <div class="services">
    <h2 class="services__title">Service times</h2>
    <p class="services__line"><span class="services__mark"></span>Sunday - 10am (<b>Sunday School</b>) 11am (<b>Family Worship</b>)<br>6pm (<b>Night of Prayer</b>)</p>
    <p class="services__line services__group"><span class="services__mark"></span>Wednesday - 7:30pm (<b>Adult Bible Study</b>)<br>Classes for all ages</p>
  </div>
</section>

<section class="card card--back">
  <div class="banner" role="img" aria-label="Photo of a worship congregation with raised hands">
    <div class="brand">
      <span class="brand__dot"></span>
      <div class="brand__text">
        <span class="brand__name">Brookvane</span>
        <span class="brand__tag">Pentecostal Church</span>
      </div>
    </div>
  </div>
  <div class="contact">
    <div class="contact__row">
      <span class="contact__item">
        <svg class="icon" viewBox="0 0 24 24"><path d="M12 2a7 7 0 0 0-7 7c0 5 7 13 7 13s7-8 7-13a7 7 0 0 0-7-7zm0 9.5A2.5 2.5 0 1 1 12 6.5a2.5 2.5 0 0 1 0 5z"/></svg>
        2718 Maple Row, Rockford, IL 61142
      </span>
    </div>
    <div class="contact__row">
      <span class="contact__item">
        <svg class="icon" viewBox="0 0 24 24" fill="none" stroke="#2a1d1a" stroke-width="1.6" style="fill:none"><circle cx="12" cy="12" r="9"/><path d="M3 12h18M12 3c3 3 3 15 0 18M12 3c-3 3-3 15 0 18M5 7h14M5 17h14"/></svg>
        brookvane.example
      </span>
      <span class="contact__item">
        <svg class="icon" viewBox="0 0 24 24"><path d="M6.6 10.8a15 15 0 0 0 6.6 6.6l2.2-2.2a1 1 0 0 1 1-.25 11.4 11.4 0 0 0 3.6.57 1 1 0 0 1 1 1V20a1 1 0 0 1-1 1A17 17 0 0 1 3 4a1 1 0 0 1 1-1h3.5a1 1 0 0 1 1 1c0 1.25.2 2.45.57 3.6a1 1 0 0 1-.25 1z"/></svg>
        815-555-0163
      </span>
    </div>
    <div class="contact__row">
      <span class="contact__item"><span class="social-dot"></span> brookvane.example</span>
      <span class="contact__item"><span class="social-dot"></span> @_brookvane</span>
    </div>
  </div>
</section>

</body>
</html>
```